KVT Business Cards

We require business cards for our business. We would like a matte black back to the card, with our logo centred in the middle. The front side of the card is open to design.

Target Market(s)

Clients looking for legal services (professional)

Industry/Entity Type

Legal

Contact Information for Business Card

Boris Telemark
Partner
Mobile: 0438 715 642
Email: boris@kvtlaw.co
Website: www.kvtlaw.co
Level 3, 118 Wexbury Street
Sydney NSW 2000

Font styles to use
Other font styles liked:
• Avenir

Colors
f04a50
ffffff
1b1b1b

Requirements
Must have
• Black back with logo included in the centre of the card.
• Our font is Avenir.

```html
<!DOCTYPE html>
<html lang="en">
<head>
<meta charset="utf-8">
<title>KVT Business Cards</title>
<link rel="stylesheet" href="https://fonts.googleapis.com/css2?family=Nunito+Sans:wght@400;700;800&display=swap">
<style>
  :root {
    --brand-red: #d61f45;
    --brand-red-dark: #b5163a;
    --ink: #1b1b1b;
    --paper: #ffffff;
    --stage: #232323;
    --plate-light: #2a2a2a;
    --plate-dark: #111111;
    --muted: #3a3a3a;
    --faint: #f3e3e7;
  }
  * { box-sizing: border-box; margin: 0; padding: 0; }
  html, body { width: 1200px; height: 960px; overflow: hidden; }
  body {
    background: var(--stage);
    font-family: "Nunito Sans", "Avenir", sans-serif;
    position: relative;
  }
  .card {
    position: absolute;
    width: 540px;
    height: 310px;
    border-radius: 4px;
    overflow: hidden;
    box-shadow: 0 18px 40px rgba(0,0,0,.45);
  }
  /* Back of card */
  .card--back { left: 620px; top: 325px; }
  .card-back__texture {
    position: absolute; inset: 0;
    background: radial-gradient(ellipse at 50% 40%, var(--plate-light), var(--plate-dark) 80%);
  }
  .card-back__brand {
    position: absolute; left: 0; right: 0; top: 96px;
    display: flex; align-items: center; justify-content: center; gap: 16px;
  }
  .brand-square {
    width: 46px; height: 46px; background: var(--brand-red);
  }
  .brand-name {
    font-weight: 800;
    font-size: 27px;
    line-height: 1.02;
    letter-spacing: .5px;
    text-transform: uppercase;
  }
  .card-back .brand-name { color: var(--paper); }
  .card-back__web {
    position: absolute; left: 0; right: 0; bottom: 74px;
    text-align: center; color: var(--paper);
    font-size: 13px; letter-spacing: 4px;
  }
  .card-back__web span { color: var(--brand-red); font-weight: 700; }

  /* Front of card */
  .card--front { left: 40px; top: 325px; background: var(--paper); }
  .card-front__band { position: absolute; inset: 0; }
  .card-front__brand {
    position: absolute; left: 26px; top: 22px;
    display: flex; align-items: center; gap: 14px;
  }
  .card-front .brand-square { width: 40px; height: 40px; }
  .card-front .brand-name { color: var(--ink); font-size: 22px; }
  .card-front__address {
    position: absolute; left: 28px; top: 122px;
    color: var(--muted); font-size: 12.5px; line-height: 1.35;
  }
  .contact-list {
    position: absolute; left: 26px; top: 196px;
    list-style: none; color: var(--paper); font-size: 12.5px;
  }
  .contact-list li { display: flex; align-items: center; gap: 8px; height: 21px; }
  .contact-list svg { width: 13px; height: 13px; flex: none; }
  .card-front__watermark {
    position: absolute; right: 46px; top: 70px;
    width: 120px; height: 120px; background: var(--faint);
  }
  .name-tab {
    position: absolute; left: 306px; top: 214px;
    width: 208px; height: 48px;
    background: linear-gradient(180deg, var(--brand-red), var(--brand-red-dark));
    border-radius: 14px;
    color: var(--paper); text-align: center;
    display: flex; flex-direction: column; justify-content: center;
  }
  .name-tab__name { font-weight: 800; font-size: 15px; letter-spacing: .4px; text-transform: uppercase; line-height: 1.1; }
  .name-tab__role { font-size: 11px; letter-spacing: .6px; text-transform: uppercase; }
</style>
</head>
<body>

  <section class="card card--front card-front" aria-label="Business card front">
    <svg class="card-front__band" viewBox="0 0 540 310" preserveAspectRatio="none" aria-hidden="true">
      <path d="M0 178 H280 C300 178 296 270 330 270 H540 V310 H0 Z" fill="var(--ink)"/>
    </svg>
    <div class="card-front__watermark" role="img" aria-label="Faint brand mark decoration"></div>

    <div class="card-front__brand">
      <span class="brand-square"></span>
      <p class="brand-name">Kane Voss<br>Telemark<br>Legal</p>
    </div>

    <p class="card-front__address">Level 3, 118 Wexbury Street<br>Sydney NSW 2000</p>

    <ul class="contact-list">
      <li>
        <svg viewBox="0 0 16 16"><circle cx="8" cy="8" r="7.2" fill="none" stroke="#fff" stroke-width="1.2"/><path d="M5.5 4.5l1.3 1.6-.8 1c.5 1 1.3 1.8 2.3 2.3l1-.8 1.6 1.3-.6 1.2C7.7 11 5 8.3 4.3 5.2z" fill="#fff"/></svg>
        0438 715 642
      </li>
      <li>
        <svg viewBox="0 0 16 16"><rect x="1.5" y="3.5" width="13" height="9" fill="none" stroke="#fff" stroke-width="1.3"/><path d="M1.5 3.5L8 9l6.5-5.5" fill="none" stroke="#fff" stroke-width="1.3"/></svg>
        boris@kvtlaw.co
      </li>
      <li>
        <svg viewBox="0 0 16 16" fill="none" stroke="#fff" stroke-width="1.1"><circle cx="8" cy="8" r="6.5"/><ellipse cx="8" cy="8" rx="3" ry="6.5"/><path d="M1.5 8h13M2.5 5h11M2.5 11h11"/></svg>
        www.kvtlaw.co
      </li>
    </ul>

    <div class="name-tab">
      <span class="name-tab__name">Boris Telemark</span>
      <span class="name-tab__role">Partner</span>
    </div>
  </section>

  <section class="card card--back card-back" aria-label="Business card back">
    <div class="card-back__texture" role="img" aria-label="Dark textured plate pattern"></div>
    <div class="card-back__brand">
      <span class="brand-square"></span>
      <p class="brand-name">Kane Voss<br>Telemark<br>Legal</p>
    </div>
    <p class="card-back__web">www.<span>kvtlaw</span>.co</p>
  </section>

</body>
</html>
```